Web Design Project!!

This is the clients current site: http://dravenhomegear.com/
I want this new design to be AMAZING! I think the current site looks fine, but the client is wanting a lot of new features added to the site so will need a new design. I need a home page design and a simple internal page also. Social media is one of the most important features of the site. Contact me with any questions. I am really just letting you all flow with this project. If you look at the clients show office location, you will see it looks amazing!
I have attached the proposal of features that are going to be needed in the site and page names.

```html
<!DOCTYPE html>
<html lang="en">
<head>
<meta charset="utf-8">
<title>Draven Home Gear</title>
<link href="https://fonts.googleapis.com/css2?family=Arimo:wght@400;700&display=swap" rel="stylesheet">
<style>
:root{
  --blue:#1b8fb3;--blue-dark:#0e6f92;--blue-light:#3db4d6;
  --olive:#4b5a0c;--text:#555;--dark:#222;
  --panel:#ebe9e0;--panel-line:#cfccc0;--band:#e3e3e3;--page:#ececec;
  --green:#8dc63f;--red:#c0302e;
}
*{margin:0;padding:0;box-sizing:border-box}
html,body{width:750px;height:1200px;overflow:hidden;background:#fff}
body{font-family:"Arimo",Arial,sans-serif;color:var(--text);font-size:9px;position:relative}
.abs{position:absolute}
.header{left:0;top:0;width:750px;height:115px;background:linear-gradient(180deg,var(--blue-light),var(--blue) 60%,var(--blue-dark))}
.brand{left:40px;top:34px;width:112px;height:40px;background:#3a322c;color:#fff;font-weight:700;font-size:18px;text-align:center;line-height:26px;letter-spacing:1px}
.brand small{display:block;font-size:7px;line-height:8px;letter-spacing:2px;font-weight:400}
.login{left:487px;top:14px;width:253px;height:86px;background:rgba(10,80,110,.45);border:1px solid rgba(255,255,255,.2);border-radius:4px}
.login h3{position:absolute;left:34px;top:10px;color:#fff;font-size:11px}
.login .lock{position:absolute;left:16px;top:7px}
.field{position:absolute;top:31px;width:112px;height:18px;background:#fff;border-radius:3px;color:#aaa;font-size:7px;line-height:18px;padding-left:14px}
.remember{position:absolute;left:62px;top:63px;color:#fff;font-size:8px}
.remember i{display:inline-block;width:7px;height:7px;background:#fff;margin-right:6px;vertical-align:-1px}
.btn-login{position:absolute;left:187px;top:60px;width:42px;height:16px;background:linear-gradient(#fff,#ccc);border-radius:3px;color:#444;font-size:9px;font-weight:700;text-align:center;line-height:16px}
.nav{left:0;top:115px;width:750px;height:40px;background:#fff;border-bottom:2px solid #d5d5d5;display:flex;align-items:center;padding-left:14px;font-size:10px;color:var(--dark)}
.nav span{margin-right:18px}
.nav .on{color:var(--blue)}
.hero{left:0;top:157px;width:750px;height:275px;background:var(--page);border-bottom:3px solid #ddd}
.box{background:var(--panel);border:1px solid var(--panel-line);border-radius:4px}
.promo{left:13px;top:173px;width:229px;height:107px}
.promo .art{position:absolute;left:8px;top:14px;width:66px;height:72px;background:linear-gradient(#a9b94a,#5f6a20);border-radius:3px}
.promo p{position:absolute;left:79px;top:17px;width:142px;font-size:9px;line-height:14px;color:#444}
.promo a{position:absolute;right:14px;top:82px;color:#555;text-decoration:underline;font-size:9px}
.news{left:13px;top:294px;width:229px;height:108px}
.news h4{position:absolute;left:8px;top:14px;color:var(--olive);font-size:11px}
.news .input{position:absolute;left:9px;top:37px;width:140px;height:20px;background:linear-gradient(#8f8f8f,#b8b8b8);border-radius:3px}
.news .sub{position:absolute;left:156px;top:38px;width:53px;height:18px;background:linear-gradient(#b7e06a,var(--green));border-radius:3px;color:var(--olive);font-weight:700;font-size:9px;text-align:center;line-height:18px}
.news p{position:absolute;left:36px;top:71px;width:180px;font-size:7px;line-height:12px;color:#666}
.news p i{position:absolute;left:-12px;top:3px;width:6px;height:6px;border:1px solid #999;background:#fff}
.slider{left:273px;top:174px;width:451px;height:225px;background:#fff;box-shadow:0 2px 6px rgba(0,0,0,.25)}
.slide-img{position:absolute;left:11px;top:12px;width:428px;height:202px;background:linear-gradient(135deg,#9aa0a4,#6a5a50 55%,#3a2a22)}
.ribbon{position:absolute;left:-2px;top:4px}
.arrow{position:absolute;width:18px;height:28px;background:#333;border-radius:14px;top:273px}
.dots{left:473px;top:412px;display:flex;gap:3px}
.dots i{width:7px;height:7px;border-radius:50%;background:#999}
.dots i.on{background:var(--green)}
.head{position:absolute;height:22px;background:var(--band);color:var(--olive);font-weight:700;font-size:12px;line-height:22px;padding-left:7px}
.head .pg{position:absolute;right:9px;top:0;font-size:10px;color:#333}
.copy{position:absolute;font-size:8.5px;line-height:13.5px;color:#555}
.thumb{position:absolute;width:74px;height:88px;background:#ddd;border:1px solid #bbb}
.thumb .ph{position:absolute;left:3px;top:3px;width:66px;height:71px}
.thumb span{position:absolute;bottom:2px;width:100%;text-align:center;font-size:8px;color:#444;font-weight:700}
.t-title{position:absolute;color:var(--olive);font-weight:700;font-size:9px}
.more{position:absolute;font-weight:700;font-size:9px;color:#333}
.date{position:absolute;width:48px;height:46px;border-radius:3px;background:#f3f3f3;box-shadow:0 1px 3px rgba(0,0,0,.3);text-align:center}
.date b{display:block;background:var(--red);color:#fff;font-size:8px;line-height:13px;border-radius:3px 3px 0 0}
.date em{font-style:normal;font-size:18px;color:#444;line-height:32px}
.grey-panel{position:absolute;background:#f0f0f0}
.gallery{left:0;top:912px;width:750px;height:222px;background:var(--page)}
.photo{position:absolute;top:951px;width:106px;height:54px;border:2px solid #bbb;border-radius:4px}
.partner{position:absolute;top:1080px;font-size:12px;font-weight:700;color:#4a4a4a}
.footer{left:0;top:1133px;width:750px;height:67px;background:linear-gradient(var(--blue),var(--blue-dark));color:#fff}
.fnav{position:absolute;left:70px;top:14px;font-size:8px;word-spacing:2px}
.fnav span{margin-right:14px}
.fbot{position:absolute;top:42px;font-size:8px}
.card{display:inline-block;width:20px;height:12px;background:#fff;border-radius:2px;margin-left:3px;vertical-align:-3px}
.soc{position:absolute;top:1168px;width:22px;height:22px;border-radius:50%;background:#fff}
</style>
</head>
<body>
<header class="abs header">
  <div class="abs brand">DRAVEN<small>HOME GEAR</small></div>
  <div class="abs login">
    <svg class="lock" width="12" height="14" viewBox="0 0 12 14"><path d="M3 6V4a3 3 0 0 1 6 0v2" stroke="#fff" stroke-width="1.6" fill="none"/><rect x="1" y="6" width="10" height="8" rx="1" fill="#fff"/></svg>
    <h3>User Log In</h3>
    <div class="field" style="left:14px">user name</div>
    <div class="field" style="left:131px">pass word</div>
    <div class="remember"><i></i>Remember my pass word</div>
    <div class="btn-login">Log in</div>
  </div>
</header>
<nav class="abs nav">
  <span class="on">Home</span><span>Company</span><span>Showroom</span><span>Testimonials</span><span>Upcoming events</span><span>Blog</span><span>Brands</span><span>Service request</span><span>Directions</span><span>Contact us</span><span>Media</span><span>Sitemap</span>
</nav>
<svg class="abs" style="left:20px;top:149px" width="12" height="6"><path d="M0 6L6 0L12 6Z" fill="#aaa"/></svg>

<section class="abs hero"></section>
<div class="abs box promo">
  <div class="art" role="img" aria-label="The Open Hearth showroom emblem"></div>
  <p>Come visit our brand new location and view the new The Open Hearth showroom. It's an experience you won't forget.</p>
  <a>Learn more...</a>
</div>
<div class="abs box news">
  <h4>NEWS LETTER</h4>
  <div class="input"></div>
  <div class="sub">Subscribe</div>
  <p><i></i>Cicero are also reproduced in their exact original form, accompanied by English</p>
</div>
<div class="abs slider">
  <div class="slide-img" role="img" aria-label="Modern kitchen with dark wood island and grey walls"></div>
  <svg class="ribbon" width="80" height="60" viewBox="0 0 80 60"><path d="M10 50L52 4H74L18 60Z" fill="#7cbf35"/><text x="30" y="40" transform="rotate(-45 30 40)" fill="#fff" font-size="8" font-weight="700" font-family="Arimo,sans-serif">WHAT'S HOT!</text></svg>
</div>
<div class="arrow" style="left:256px"><svg width="18" height="28"><path d="M11 9L6 14L11 19" stroke="#fff" stroke-width="2" fill="none"/></svg></div>
<div class="arrow" style="left:722px"><svg width="18" height="28"><path d="M7 9L12 14L7 19" stroke="#fff" stroke-width="2" fill="none"/></svg></div>
<div class="abs dots"><i></i><i></i><i class="on"></i><i></i><i></i></div>

<!-- Welcome -->
<div class="head" style="left:22px;top:446px;width:322px">Welcome To Our Site</div>
<p class="copy" style="left:22px;top:475px;width:322px">The standard chunk of Lorem Ipsum used since the 1500s is reproduced below for those interested. Sections 1.10.32 and 1.10.33 from "de Finibus Bonorum et Malorum" by Cicero are also reproduced in their exact original form, accompanied by English versions from the 1914 translation by H. Rackham.</p>

<div class="head" style="left:22px;top:547px;width:322px">Latest Cooking Events<span class="pg">&lt; &gt;</span></div>
<div class="thumb" style="left:22px;top:579px"><div class="ph" role="img" aria-label="Grey modern kitchen" style="background:linear-gradient(#cfd3d6,#555)"></div><span>Lorem Ipsum</span></div>
<div class="t-title" style="left:106px;top:580px">The standard chunk of Lorem Ipsum</div>
<p class="copy" style="left:106px;top:600px;width:236px">Sections 1.10.32 and 1.10.33 from "de Finibus Bonorum et Malorum" by Cicero are also reproduced.</p>
<div class="more" style="left:289px;top:638px">Read more</div>
<div class="thumb" style="left:22px;top:662px"><div class="ph" role="img" aria-label="Kitchen with orange cabinets" style="background:linear-gradient(#d9d2c4,#e08a2a)"></div><span>Lorem Ipsum</span></div>
<div class="t-title" style="left:106px;top:663px">The standard chunk of Lorem Ipsum</div>
<p class="copy" style="left:106px;top:684px;width:236px">Sections 1.10.32 and 1.10.33 from "de Finibus Bonorum et Malorum" by Cicero are also reproduced.</p>
<div class="more" style="left:289px;top:721px">Read more</div>

<div class="head" style="left:22px;top:755px;width:322px">Upcoming Events<span class="pg">&lt; &gt;</span></div>
<div class="date" style="left:40px;top:789px"><b>Sep 2011</b><em>12</em></div>
<div class="t-title" style="left:106px;top:787px">The standard chunk of Lorem Ipsum</div>
<p class="copy" style="left:106px;top:807px;width:236px">Sections 1.10.32 and 1.10.33 from "de Finibus Bonorum et Malorum" by Cicero are also reproduced.</p>
<div class="date" style="left:40px;top:852px"><b>Sep 2011</b><em>12</em></div>
<div class="t-title" style="left:106px;top:849px">The standard chunk of Lorem Ipsum</div>
<p class="copy" style="left:106px;top:869px;width:236px">Sections 1.10.32 and 1.10.33 from "de Finibus Bonorum et Malorum" by Cicero are also reproduced.</p>

<!-- Right column -->
<div class="head" style="left:360px;top:446px;width:364px">Latest Video</div>
<p class="copy" style="left:367px;top:485px;width:155px;font-size:8px;line-height:13px;color:#777">The standard chunk of Lorem Ipsum used since the 1500s is reproduced below for those interested. Sections 1.10.32 and 1.10.33 from "de Finibus Bonorum et Malorum" by Cicero.</p>
<div class="abs" role="img" aria-label="Video still of a blue-lit kitchen" style="left:530px;top:478px;width:183px;height:112px;background:linear-gradient(135deg,#dfe6ee,#4a66c8 60%,#2a3a8a)"></div>
<div class="abs" style="left:530px;top:590px;width:183px;height:10px;background:#ddd"><div style="margin:4px 0 0 16px;width:80px;height:2px;background:var(--red)"></div></div>

<div class="grey-panel" style="left:360px;top:618px;width:364px;height:120px"></div>
<div class="head" style="left:360px;top:618px;width:364px">Testimonials<span class="pg">&lt; &gt;</span></div>
<div class="abs" role="img" aria-label="Customer avatar" style="left:368px;top:651px;width:58px;height:58px;background:linear-gradient(#3d4a5a,#1e2833);border:2px solid #fff;box-shadow:0 0 2px #999"></div>
<div class="abs" style="left:375px;top:713px;font-size:9px;font-weight:700;color:#333">RJ Talmon</div>
<div class="abs" style="left:434px;top:650px;font-size:9px;font-weight:700;color:#333">Lorem Ipsum Contantry Dummy Text</div>
<p class="copy" style="left:434px;top:670px;width:284px">Sections 1.10.32 and 1.10.33 from "de Finibus Bonorum et Malorum" by Cicero are also reproduced in their exact original form, accompanied by English versions from the 1914 translation by H. Rackham.</p>
<div class="more" style="left:670px;top:723px;color:#555">View more</div>

<div class="grey-panel" style="left:360px;top:755px;width:364px;height:138px"></div>
<div class="head" style="left:360px;top:755px;width:364px">Our Blog</div>
<div class="abs" role="img" aria-label="Blog post preview screenshot" style="left:370px;top:788px;width:125px;height:72px;background:linear-gradient(135deg,#eee,#2a3a7a 50%,#c8c8c8);border:2px solid #ccc;border-radius:4px"></div>
<div class="abs" style="left:505px;top:792px;font-size:9px;font-weight:700;color:#333">Lorem Ipsum Contantry Dummy Text</div>
<p class="copy" style="left:505px;top:812px;width:212px">Sections 1.10.32 and 1.10.33 from "de Finibus Bonorum et Malorum" by Cicero are also reproduced in their exact original form, accompanied.</p>
<div class="more" style="left:666px;top:864px;color:#555">View more</div>

<!-- Gallery & partners -->
<section class="abs gallery"></section>
<div class="head" style="left:22px;top:919px;width:704px;background:#d9d9d9">Photo</div>
<svg class="abs" style="left:34px;top:968px" width="12" height="18"><path d="M10 2L3 9L10 16" stroke="#777" stroke-width="3" fill="none"/></svg>
<svg class="abs" style="left:702px;top:968px" width="12" height="18"><path d="M2 2L9 9L2 16" stroke="#777" stroke-width="3" fill="none"/></svg>
<div class="photo" role="img" aria-label="Kitchen photo" style="left:57px;background:linear-gradient(#d8d2c8,#7a6a5a)"></div>
<div class="photo" role="img" aria-label="Kitchen photo" style="left:193px;background:linear-gradient(#c9a98a,#5a4030)"></div>
<div class="photo" role="img" aria-label="Kitchen photo" style="left:327px;background:linear-gradient(#bbb,#333)"></div>
<div class="photo" role="img" aria-label="Kitchen photo" style="left:456px;background:linear-gradient(#c8b0c8,#8a6a7a)"></div>
<div class="photo" role="img" aria-label="Kitchen photo" style="left:584px;background:linear-gradient(#eee,#6a5a4a)"></div>
<div class="head" style="left:22px;top:1025px;width:704px;background:#d9d9d9">Our Partners</div>
<div class="partner" style="left:45px">Oakline</div>
<div class="partner" style="left:145px">Stirwell</div>
<div class="partner" style="left:232px">Pantrico</div>
<div class="partner" style="left:318px">Brenmoor</div>
<div class="partner" style="left:420px">Calder Works</div>
<div class="partner" style="left:550px">Ashgrove</div>
<div class="partner" style="left:626px">Veltro Studio</div>

<footer class="abs footer">
  <div class="fnav"><span>Home</span><span>Company</span><span>Showroom</span><span>Testimonials</span><span>Upcoming events</span><span>Blog</span><span>Brands</span><span>Service request</span><span>Directions</span><span>Contact us</span><span>Media</span><span>Sitemap</span></div>
  <div class="fbot" style="left:40px">Copyright @ 2011 www.dravenhomegear.com All rights reserved</div>
  <div class="fbot" style="left:314px">Payments : <i class="card"></i><i class="card"></i><i class="card"></i><i class="card"></i></div>
  <div class="fbot" style="left:495px">Connect with us :</div>
</footer>
<div class="soc" style="left:565px"></div>
<div class="soc" style="left:596px"></div>
<div class="soc" style="left:627px"></div>
<div class="soc" style="left:657px"></div>
<div class="soc" style="left:688px"></div>
</body>
</html>
```